Defend science flier

Put my name and text below on one side of flier, and place other text on other side. Try to keep file about 4 by 6 or 6 by 8 inches.

Target Market(s)

Community and retailers.

Industry/Entity Type

Retail and concerned community.

Font styles to use
Serif

Requirements
Must have
• Good, eye-catching titles. Be smaller format. Not 8 by 11
Nice to have
• Black and white text. Maybe bullets etc for organizion but no decorations.
Should not have
• Any decoration

```html
<!DOCTYPE html>
<html lang="en">
<head>
<meta charset="utf-8">
<title>Martin Oldenkamp – Defend Science Flier</title>
<link rel="stylesheet" href="https://fonts.googleapis.com/css2?family=Oswald:wght@600&family=Jost:wght@700&family=Montserrat:ital,wght@0,300;0,400;0,600;0,700;1,300&display=swap">
<style>
  :root {
    --backdrop: #7a7a7a;
    --ink-dark: #1f1f20;
    --gold: #a88a4a;
    --navy: #2a2d3d;
    --white: #ffffff;
    --soft-white: #e9e9e9;
  }
  * { margin: 0; padding: 0; box-sizing: border-box; }
  html, body { width: 1200px; height: 1200px; overflow: hidden; }
  body {
    background: var(--backdrop);
    font-family: "Montserrat", Arial, sans-serif;
    position: relative;
  }
  .flier {
    position: absolute;
    top: 227px;
    width: 497px;
    height: 746px;
    background: var(--ink-dark);
    overflow: hidden;
  }
  .flier--front { left: 76px; }
  .flier--back { left: 636px; }
  .flier__shape { position: absolute; inset: 0; }

  /* Front */
  .name {
    position: absolute;
    right: 38px;
    top: 50px;
    text-align: right;
    font-family: "Oswald", "Arial Narrow", sans-serif;
    font-weight: 600;
    color: var(--gold);
    font-size: 45px;
    line-height: 42px;
    letter-spacing: 0;
    transform: scaleX(0.9);
    transform-origin: right top;
  }
  .credential {
    position: absolute;
    right: 38px;
    top: 140px;
    font-family: "Montserrat", sans-serif;
    font-weight: 700;
    font-size: 22px;
    line-height: 24px;
    color: var(--navy);
  }
  .tagline {
    position: absolute;
    left: 0; right: 0;
    top: 328px;
    text-align: center;
    color: var(--white);
    font-size: 17px;
    line-height: 21px;
    font-weight: 400;
  }
  .quote-mark {
    font-family: "Jost", sans-serif;
    font-weight: 700;
    color: var(--white);
    font-size: 34px;
    line-height: 0;
    position: relative;
  }
  .quote-mark--open { top: 8px; margin-right: 6px; }
  .quote-mark--close { top: 20px; margin-left: 6px; }
  .bio-tab {
    position: absolute;
    left: 38px; top: 408px;
    width: 23px; height: 77px;
    background: var(--gold);
    border-radius: 12px;
  }
  .bio-tab span {
    position: absolute;
    left: 50%; top: 50%;
    transform: translate(-50%, -50%) rotate(-90deg);
    white-space: nowrap;
    color: var(--white);
    font-weight: 700;
    font-size: 10.5px;
  }
  .bio {
    position: absolute;
    left: 73px; right: 33px; top: 410px;
    color: var(--soft-white);
    font-size: 12.9px;
    line-height: 16.5px;
    font-weight: 300;
  }
  .bio p + p { margin-top: 7px; }
  .bio p:last-child { text-align: justify; text-align-last: left; }
  .endorsement {
    position: absolute;
    left: 0; right: 0; top: 525px;
    text-align: center;
    color: var(--white);
    font-weight: 600;
    font-size: 13.3px;
    line-height: 17px;
  }
  .testimonial {
    position: absolute;
    left: 48px; right: 50px; top: 582px;
    text-align: center;
    color: var(--soft-white);
    font-style: italic;
    font-weight: 300;
    font-size: 10.2px;
    line-height: 12.5px;
  }
  .testimonial .quote-mark { font-size: 24px; font-style: normal; }
  .testimonial .quote-mark--open { top: 5px; margin-right: 4px; }
  .testimonial .quote-mark--close { top: 12px; margin-left: 4px; }
  .rule {
    position: absolute;
    left: 29px; right: 28px; top: 656px;
    height: 1px;
    background: var(--gold);
  }
  .contact {
    position: absolute;
    left: 0; right: 0; top: 678px;
    text-align: center;
    color: var(--white);
    font-weight: 600;
    font-size: 13.6px;
    line-height: 17px;
  }
  .contact__url { color: var(--gold); display: block; }

  /* Back */
  .headline {
    position: absolute;
    left: 62px; top: 30px;
    display: flex; align-items: center;
    font-family: "Jost", sans-serif;
    font-weight: 700;
    font-size: 21px;
    letter-spacing: 0.3px;
  }
  .headline__pill {
    background: var(--gold);
    color: var(--white);
    border-radius: 16px;
    padding: 3px 12px;
    margin-right: 9px;
  }
  .headline__rest { color: var(--gold); }
  .lead {
    position: absolute;
    left: 0; right: 0; top: 78px;
    text-align: center;
    color: var(--ink-dark);
    font-weight: 700;
    font-size: 12.6px;
    line-height: 16.5px;
  }
  .sins { position: absolute; list-style: none; color: var(--ink-dark); font-size: 13.4px; line-height: 16.7px; font-weight: 400; }
  .sin { position: absolute; padding-left: 22px; }
  .sin__num {
    position: absolute; left: 0; top: 1px;
    width: 15px; height: 15px; border-radius: 50%;
    background: var(--navy); color: var(--white);
    font-size: 10px; font-weight: 700; line-height: 15px; text-align: center;
  }
  .body-copy {
    position: absolute;
    left: 55px; right: 45px; top: 438px;
    color: var(--soft-white);
    font-weight: 300;
    font-size: 13.4px;
    line-height: 16.6px;
  }
  .body-copy p + p { margin-top: 16px; }
</style>
</head>
<body>

<section class="flier flier--front">
  <svg class="flier__shape" viewBox="0 0 497 746" aria-hidden="true">
    <defs>
      <linearGradient id="colonnade-tone" x1="0" y1="0" x2="1" y2="0">
        <stop offset="0" stop-color="#b4b4b4"/>
        <stop offset="0.45" stop-color="#d6d6d6"/>
        <stop offset="0.75" stop-color="#f7f7f7"/>
        <stop offset="1" stop-color="#ffffff"/>
      </linearGradient>
    </defs>
    <path fill="var(--gold)" d="M0 0 H497 V270 C410 296 310 308 240 302 C130 292 40 210 0 124 Z"/>
    <path fill="url(#colonnade-tone)" role="img" aria-label="Photo of classical stone columns fading to white"
          d="M0 0 H497 V171 C390 228 260 268 160 259 C90 252 35 220 0 177 Z"/>
  </svg>

  <h1 class="name">MARTIN<br>OLDENKAMP</h1>
  <div class="credential">PH.D.</div>

  <p class="tagline"><span class="quote-mark quote-mark--open">“</span>The Vellacourt and<br>Ashmore of Psychology and History.<span class="quote-mark quote-mark--close">”</span></p>

  <div class="bio-tab"><span>Martin's Bio</span></div>
  <div class="bio">
    <p>Psych has Restructured the Liberal Arts and Sciences—from Genetics to the Fine Arts and Hollywood.</p>
    <p>Museum Catalogues, Better Nonfiction, and Hollywood Films Now Use Martin’s Methods.</p>
  </div>

  <p class="endorsement">Martin’s Biopsych is endorsed by Dr. R. Elliot Marsh, professor<br>of psychiatry at Northfield Medical School, who said:</p>

  <p class="testimonial"><span class="quote-mark quote-mark--open">“</span>Modern sleep and dream research teaches us—as does Martin Oldenkamp’s book Inner Sin or Civic Sin—that all human activities, including art and politics, are products of the human brain, and that each of us has the privilege and responsibility of using it and communicating its creations.<span class="quote-mark quote-mark--close">”</span></p>

  <div class="rule"></div>
  <p class="contact">See Martin’s homepage for more details:<span class="contact__url">www.martin-oldenkamp.org</span></p>
</section>

<section class="flier flier--back">
  <svg class="flier__shape" viewBox="0 0 497 746" aria-hidden="true">
    <defs>
      <radialGradient id="sketch-tone" cx="0.5" cy="0.5" r="0.55">
        <stop offset="0" stop-color="#efe1c6"/>
        <stop offset="0.75" stop-color="#d9c19a"/>
        <stop offset="1" stop-color="#b8976a"/>
      </radialGradient>
    </defs>
    <path fill="var(--gold)" d="M0 0 H497 V366 C420 385 300 400 210 394 C110 386 35 320 0 242 Z"/>
    <path fill="var(--white)" d="M0 0 H497 V270 C420 320 300 362 190 364 C100 366 30 300 0 220 Z"/>
    <circle cx="132" cy="328" r="82" fill="var(--gold)"/>
    <circle cx="132" cy="328" r="75" fill="var(--white)"/>
    <circle cx="132" cy="328" r="72" fill="url(#sketch-tone)" role="img" aria-label="Renaissance anatomical sketch of human proportions"/>
  </svg>

  <h2 class="headline"><span class="headline__pill">WHY DID</span><span class="headline__rest">THE CULTURE CHANGE?</span></h2>
  <p class="lead">During the 1960s, we socialized the Seven Deadly Sins.<br>Therefore:</p>

  <ol class="sins">
    <li class="sin" style="left:45px;top:136px;width:200px;"><span class="sin__num">1</span>Pride became “Racism.”</li>
    <li class="sin" style="left:45px;top:170px;width:186px;"><span class="sin__num">2</span>Lust became “Sexism” and “Gender“ existing “out there.”</li>
    <li class="sin" style="left:264px;top:136px;width:215px;"><span class="sin__num">3</span>Gluttony became “Consumer Fetishism.”</li>
    <li class="sin" style="left:264px;top:186px;width:215px;"><span class="sin__num">4</span>Vanity became “Media Images of Beauty.”</li>
    <li class="sin" style="left:264px;top:235px;width:215px;"><span class="sin__num">5</span>Sloth became The lack of social action: “Are you fighting for diversity?”</li>
  </ol>

  <div class="body-copy">
    <p>This “fight for diversity” inspires attacks against people like Dr. Oldenkamp for asserting any reality principle about human nature.</p>
    <p>These thugs are religious crusaders who ignore the rule of law and try to stop the progress of science. These fanatics go around and give people a “tear-test”—as during the Salem witch trials. Don’t let them take over.</p>
    <p>The educational and culture elites—such as<br>Hollywood—now reject these theological “social sins.” The elites are replacing theology with traditional,<br>human-based sin.</p>
  </div>

  <p class="contact">See Martin’s homepage for more details:<span class="contact__url">www.martin-oldenkamp.org</span></p>
</section>

</body>
</html>
```